Kelvar Systems Website

Website design for our company: Kelvar Systems.
The website should look fresh and IT focused. Please have a look at http://www.kelvarsystems.net.au/ for our current design. We want something fresh and new, professional looking, in WordPress so we can easily make changes.

Industry/Entity Type

It Company

```html
<!DOCTYPE html>
<html lang="en">
<head>
<meta charset="utf-8">
<title>Kelvar Systems – IT Solutions</title>
<link href="https://fonts.googleapis.com/css2?family=Exo+2:ital,wght@0,700;0,800;1,700;1,800;1,900&family=Arimo:ital,wght@0,400;0,700;1,400&display=swap" rel="stylesheet">
<style>
:root{
  --green:#0fae52;
  --green-light:#22c765;
  --green-dark:#0a8a40;
  --panel:rgba(0,80,35,.28);
  --panel-deep:rgba(0,60,25,.38);
  --blue:#1572c9;
  --blue-dark:#0b4f9a;
  --white:#ffffff;
  --mint:#5ff59a;
  --header-top:#ffffff;
  --header-bottom:#d6d6d6;
}
*{box-sizing:border-box;margin:0;padding:0}
html,body{width:1200px;height:1018px;overflow:hidden}
body{
  position:relative;
  font-family:"Arimo",Arial,sans-serif;
  color:var(--white);
  background:radial-gradient(ellipse at 55% 45%,var(--green-light) 0%,var(--green) 45%,var(--green-dark) 100%);
}
.site-header{
  position:absolute;left:0;top:0;width:1200px;height:117px;
  background:linear-gradient(var(--header-top) 0%,#f1f1f1 50%,#e2e2e2 52%,var(--header-bottom) 100%);
  box-shadow:0 3px 6px rgba(0,0,0,.25);
}
.brand{
  position:absolute;left:128px;top:40px;display:flex;align-items:center;gap:12px;
}
.brand-mark{width:34px;height:34px;border-radius:50%;background:var(--green)}
.brand-name{font-family:"Exo 2",sans-serif;font-weight:800;font-size:24px;color:var(--green-dark)}
.main-nav{position:absolute;left:415px;top:50px;display:flex}
.main-nav a{
  font-family:"Exo 2",sans-serif;font-style:italic;font-weight:800;font-size:14px;
  color:var(--blue);text-decoration:none;padding:0 13px;border-left:1px solid #c4c4c4;line-height:20px;
}
.main-nav a:first-child{border-left:none}

.intro{position:absolute;left:104px;top:117px;width:1003px;height:257px;background:var(--panel)}
.feature{position:absolute;top:19px}
.feature-icon{
  width:60px;height:60px;border-radius:8px;
  background:linear-gradient(#3aa2f2,var(--blue-dark));
  box-shadow:0 2px 4px rgba(0,0,0,.3);display:flex;align-items:center;justify-content:center;
}
.feature-title{
  position:absolute;left:70px;top:38px;white-space:nowrap;
  font-family:"Exo 2",sans-serif;font-style:italic;font-weight:800;font-size:19px;letter-spacing:.3px;
}
.feature-rule{width:100%;height:1px;background:rgba(255,255,255,.3);margin-top:14px}
.feature-body{font-size:12px;line-height:14px;margin-top:14px;text-align:justify}
.feature-body p+p{margin-top:14px}
.feature-body ul{list-style:none;margin:12px 0 0 36px;text-align:left}

.testimonials{position:absolute;left:698px;top:0;width:305px;height:257px;background:var(--panel-deep);padding:19px 18px 0 18px}
.testimonials h2{
  font-family:"Exo 2",sans-serif;font-style:italic;font-weight:800;font-size:17px;
  display:flex;align-items:center;gap:6px;margin-bottom:8px;
}
.quote{margin-bottom:12px;font-size:12.5px;line-height:15px}
.quote cite{display:block;font-style:italic}
.quote a{color:var(--mint)}

.hero-art{
  position:absolute;left:125px;top:382px;width:410px;height:256px;border-radius:6px;
  background:linear-gradient(90deg,#1f7fe0 0%,#2a6cc4 30%,#2b2f36 45%,#4c5058 70%,#25282d 100%);
  opacity:.9;
}
.hero-copy{position:absolute;left:573px;top:412px;width:520px}
.hero-copy h1{
  font-family:"Exo 2",sans-serif;font-style:italic;font-weight:900;font-size:43px;line-height:38px;
  letter-spacing:1px;text-shadow:0 2px 4px rgba(0,0,0,.25);
}
.hero-copy p{font-style:italic;font-size:18px;line-height:22px;margin-top:24px}

.sectors{position:absolute;left:104px;top:644px;width:1003px;height:258px;background:var(--panel)}
.sector{position:absolute;top:25px;width:224px}
.sector-icon{
  width:78px;height:78px;margin-left:61px;border-radius:9px;border:2px solid rgba(255,255,255,.6);
  background:linear-gradient(var(--green-light),var(--green-dark));display:flex;align-items:center;justify-content:center;
}
.sector-icon span{width:50px;height:50px;border-radius:50%;display:block}
.sector h3{font-family:"Exo 2",sans-serif;font-weight:800;font-size:14.5px;letter-spacing:.6px;margin-top:16px}
.sector p{font-size:12.5px;line-height:15.5px;margin-top:16px;text-align:justify}
.sector a{font-size:12.5px;color:var(--mint);text-decoration:none}

.site-footer{position:absolute;left:0;top:915px;width:1200px;height:70px}
.footer-brand{position:absolute;left:128px;top:20px;display:flex;align-items:center;gap:7px}
.footer-brand .brand-mark{width:18px;height:18px;background:var(--green-dark)}
.footer-brand .brand-name{font-size:13px;color:var(--white)}
.footer-legal{
  position:absolute;left:280px;top:10px;height:42px;border-left:1px solid rgba(255,255,255,.3);
  padding:8px 0 0 17px;font-size:10px;font-weight:700;line-height:13px;
}
.footer-links{
  position:absolute;left:809px;top:10px;height:42px;border-left:1px solid rgba(255,255,255,.3);
  padding:14px 0 0 29px;font-size:10.5px;font-weight:700;white-space:nowrap;
}
.footer-links a{color:var(--white);text-decoration:none}
.footer-links span{margin:0 7px}
</style>
</head>
<body>
<header class="site-header">
  <div class="brand"><span class="brand-mark"></span><span class="brand-name">Kelvar Systems</span></div>
  <nav class="main-nav">
    <a href="#">HOME</a><a href="#">CLIENTS</a><a href="#">SERVICES</a><a href="#">SUPPORTS</a><a href="#">TESTIMONIALS</a><a href="#">CONTACT US</a><a href="#">ABOUT US</a>
  </nav>
</header>

<section class="intro">
  <div class="feature" style="left:16px;width:207px">
    <div class="feature-icon"><svg width="30" height="36" viewBox="0 0 30 36" fill="none" stroke="#fff" stroke-width="3"><path d="M9 25c0-5-6-7-6-13a12 12 0 0 1 24 0c0 6-6 8-6 13z"/><path d="M10 30h10M11 34h8"/></svg></div>
    <div class="feature-title">WHAT WE DU</div>
    <div class="feature-rule"></div>
    <div class="feature-body">
      <p>Kelvar Systems is an Adelaide based company with a single objective - to excel in the support and service of all computer and IT needs.</p>
      <p>We provide a high level of consulting services using the most experienced engineers at a reasonable and fair price.</p>
    </div>
  </div>
  <div class="feature" style="left:246px;width:209px">
    <div class="feature-icon"><svg width="36" height="36" viewBox="0 0 36 36" fill="none" stroke="#fff" stroke-width="4" stroke-linecap="round"><path d="M7 29 24 12M22 6l8 8M8 8l21 21M5 11l6-6"/></svg></div>
    <div class="feature-title">OUR SERVICES</div>
    <div class="feature-rule"></div>
    <div class="feature-body">
      <p><b>Internet:</b> The server can act as a gateway between your office network and the Internet.</p>
      <p><b>Security:</b> Data is stored at a central point on the server</p>
      <p><b>Backup:</b> The server can be used to backup all data stored on the network to a single point,</p>
    </div>
  </div>
  <div class="feature" style="left:477px;width:215px">
    <div class="feature-icon"><svg width="36" height="36" viewBox="0 0 36 36"><circle cx="18" cy="18" r="11" fill="none" stroke="#fff" stroke-width="7" stroke-dasharray="5 3.6"/><circle cx="18" cy="18" r="8" fill="none" stroke="#fff" stroke-width="4"/></svg></div>
    <div class="feature-title">OUR SUPPORTS</div>
    <div class="feature-rule"></div>
    <div class="feature-body">
      <p>At Kelvar Systems we provide the best</p>
      <ul><li>*Local Support</li><li>*On-Site Support</li><li>*Local Remote Support</li><li>*Support with Server/<br>&nbsp;Workstation Backup</li></ul>
    </div>
  </div>
  <aside class="testimonials">
    <h2><svg width="28" height="26" viewBox="0 0 28 26" fill="#fff"><path d="M3 2 6 25" stroke="#fff" stroke-width="2.5"/><path d="M4 3c8-4 12 5 22 1l-4 7 3 6c-9 4-13-5-19-1z"/></svg>LATEST TESTIMONIALS</h2>
    <div class="quote"><cite>Marta Quill</cite>Pellentesque augue nunc, volutpat ac fringilla ut, aliquet nec risus. <a href="#">read more</a> &gt;</div>
    <div class="quote"><cite>Darren Holloway</cite>Pellentesque augue nunc, volutpat ac fringilla ut, aliquet nec risus. <a href="#">read more</a> &gt;</div>
    <div class="quote"><cite>Irene Castell</cite>Pellentesque augue nunc, volutpat ac fringilla ut, aliquet nec risus. <a href="#">read more</a> &gt;</div>
  </aside>
</section>

<div class="hero-art" role="img" aria-label="Blue globe beside a row of server racks"></div>
<div class="hero-copy">
  <h1>AT KELVAR SYSTEMS<br>WE PROVIDE THE BEST</h1>
  <p>We specialise in building, installing and managing customised servers for businesses of all sizes. Servers can be managed at your premises or ours.</p>
</div>

<section class="sectors">
  <div class="sector" style="left:32px">
    <div class="sector-icon"><span role="img" aria-label="Golden globe with banknotes" style="background:radial-gradient(#ffe27a,#c8901c)"></span></div>
    <h3>FINANCIAL INSTITUTIONS</h3>
    <p>Lorem ipsum dolor sit amet, consectetur adipiscing elit. Donec turpis neque, sodales a faucibus at, viverra luctus urna.</p>
    <a href="#">Read More</a>
  </div>
  <div class="sector" style="left:272px">
    <div class="sector-icon"><span role="img" aria-label="Golden padlock" style="background:radial-gradient(#ffe27a,#b8860b)"></span></div>
    <h3>INSURANCES</h3>
    <p>Lorem ipsum dolor sit amet, consectetur adipiscing elit. Donec turpis neque, sodales a faucibus at, viverra luctus urna.</p>
    <a href="#">Read More</a>
  </div>
  <div class="sector" style="left:512px">
    <div class="sector-icon"><span role="img" aria-label="Pharmacy mortar with red heart" style="background:radial-gradient(#ffffff,#d8333a)"></span></div>
    <h3>PHARMACIES</h3>
    <p>Lorem ipsum dolor sit amet, consectetur adipiscing elit. Donec turpis neque, sodales a faucibus at, viverra luctus urna.</p>
    <a href="#">Read More</a>
  </div>
  <div class="sector" style="left:752px">
    <div class="sector-icon"><span role="img" aria-label="House with green roof" style="background:radial-gradient(#ffffff,#5aa84a)"></span></div>
    <h3>REAL ESTATE</h3>
    <p>Lorem ipsum dolor sit amet, consectetur adipiscing elit. Donec turpis neque, sodales a faucibus at, viverra luctus urna.</p>
    <a href="#">Read More</a>
  </div>
</section>

<footer class="site-footer">
  <div class="footer-brand"><span class="brand-mark"></span><span class="brand-name">Kelvar Systems</span></div>
  <div class="footer-legal">COPYRIGHT © 2014 KELVAR SYSTEMS PTY LTD. ALL RIGHTS RESERVED.<br>27 HARBOUR LANE KINGSFORD WEST 5011 - AUSTRALIA</div>
  <div class="footer-links"><a href="#">MAPA SITE</a><span>|</span><a href="#">POLITIC PROVACY</a><span>|</span><a href="#">CONTACT US</a></div>
</footer>
</body>
</html>
```